RidgeHornSupply.com

I need a new webdesign for a company in the San Jose/SF Bay area that showcases the financial benefits of buying used band instruments for junior high students.This would be opposed to the current and costly option of renting cheap quality instruments from the 2 or 3 local music stores that charge a monthly fee that over the years charges the buyer 3 or 4x over..
Instruments: focus in on Alto Sax, Trumpet, Flute, Clarinet, Trombone, Tenor Sax, Baritone
Target middle schools are Kestrelwood Middle School and Harlow Middle School in San Jose, CA. Both have award winning band programs.
Files attached may or may not be important.
Tabs Needed and funtional
Contact
Shopping Cart
Select Instrument
Checkout
Add to Cart, etc.
Instuments
quantity, etc.
trade in your instrument/sell your instrument
ability to add or take away new instruments for sale. including pictures
Additional questions or info, feel free to ask
Hi Designers,
Project Deadline Extended
Reason: In the next week you will be receiving specific content that will be required to be had on the website.
New desigins are still welcome. Please continue to contact me if you have questions about your individual designs.
Thanks!
Ridge Horn

```html
<!DOCTYPE html>
<html lang="en">
<head>
<meta charset="utf-8">
<title>Ridge Horn Instruments</title>
<link href="https://fonts.googleapis.com/css2?family=Open+Sans:wght@400;600;700&display=swap" rel="stylesheet">
<style>
:root{
  --gold:#e1b43a;
  --gold-light:#f3cf5d;
  --gold-dark:#b8892a;
  --tan:#c5a87c;
  --tan-dark:#a98a5c;
  --ink:#2b2b2b;
  --muted:#555;
  --orange:#f2a21c;
  --green:#3aa12c;
  --red:#e32222;
  --line:#dcdcdc;
  --navy:#1d2430;
}
*{box-sizing:border-box;margin:0;padding:0}
html,body{width:1093px;height:1200px;overflow:hidden}
body{font-family:"Open Sans",sans-serif;color:var(--ink);position:relative;background:#f4f4f2}
.backdrop{position:absolute;inset:0;background:linear-gradient(180deg,#7d8a86 0%,#8a8f7e 25%,#6f8a52 45%,#9db07a 55%,#f4f4f2 65%)}
.page{position:absolute;left:166px;top:0;width:761px;height:1200px;background:#fbfbfa}
.abs{position:absolute}
.logo{left:190px;top:44px;font-size:30px;font-weight:600;color:var(--ink);display:flex;align-items:center;gap:10px;letter-spacing:1px}
.logo .dot{width:28px;height:28px;border-radius:50%;background:var(--gold)}
.toplinks{top:33px;left:515px;font-size:8px;color:var(--ink);display:flex;gap:22px}
.toplinks .login{color:var(--orange)}
.currency{top:31px;left:892px;font-size:11px}
.phone{top:60px;left:790px;font-size:17px;color:var(--green);display:flex;align-items:center;gap:8px}
.nav{left:166px;top:103px;width:761px;height:30px;background:linear-gradient(180deg,var(--gold-light),var(--gold));display:flex}
.nav a{color:#fff;font-size:12px;font-weight:600;text-decoration:none;line-height:30px;border-right:1px solid #8a6a20;padding:0 20px}
.search{left:741px;top:108px;width:169px;height:21px;background:#fff;border-radius:2px;font-size:8px;color:#888;padding:5px 10px}
.slide{left:182px;top:152px;width:506px;height:231px;background:linear-gradient(135deg,#e9dcb8,#c9a24a 40%,#8a3a18 65%,#f2efe8)}
.caption{left:182px;top:383px;width:506px;height:45px;background:#eeebe6;font-size:11px;font-weight:600;padding:15px 13px}
.arrowbtn{top:395px;width:22px;height:22px;background:#555;color:#fff;font-size:12px;text-align:center;line-height:22px}
.promo{left:708px;width:200px;color:#fff}
.promo .head{position:absolute;left:60px;top:0;width:140px;height:46px;font-size:11px;padding:10px 15px;line-height:1.2}
.promo .head b{display:block;text-align:right;font-size:14px;font-weight:600;letter-spacing:.5px}
.promo .body{position:absolute;left:0;top:46px;width:200px;font-size:7.5px;padding:20px 14px;line-height:1.45}
.promo .go{position:absolute;right:0;bottom:0;width:30px;height:18px;background:#fff;color:var(--red);font-size:12px;text-align:center;line-height:18px}
.barhead{height:31px;color:#fff;font-size:14px;font-weight:600;padding:6px 12px;letter-spacing:.3px}
.cats{left:182px;top:508px;width:203px;height:241px;background:#fff;border:1px solid var(--line);padding:10px 8px;font-size:9px;list-style:none}
.cats li{height:23px;line-height:16px}
.cats li::before{content:"» ";color:var(--green)}
.card{width:147px;height:244px;background:#fff;border:1px solid var(--line);box-shadow:0 1px 3px rgba(0,0,0,.08)}
.card .img{position:absolute;left:10px;top:8px;width:127px;height:122px;background:radial-gradient(ellipse,#d8b456,#f7f2e4 70%)}
.card .stars{position:absolute;left:6px;top:133px;color:var(--orange);font-size:11px;letter-spacing:1px}
.card h3{position:absolute;left:6px;top:148px;font-size:12px;font-weight:600;color:var(--orange)}
.card p{position:absolute;left:7px;top:165px;font-size:7.5px;line-height:1.45;color:var(--ink)}
.card .price{position:absolute;left:8px;top:193px;font-size:12px;font-weight:600}
.card .cart{position:absolute;left:5px;top:216px;width:78px;height:19px;background:var(--navy);color:#fff;font-size:7.5px;font-weight:600;line-height:19px;padding-left:26px;border-radius:2px}
.card .mini{position:absolute;top:217px;width:18px;height:18px;border:1px solid #bbb;font-size:9px;color:var(--green);text-align:center;line-height:16px}
.news{left:182px;top:781px;width:203px;height:248px;background:linear-gradient(180deg,#b58e38,#dcb64a);color:#fff}
.news .head{position:absolute;left:53px;top:0;width:150px;height:42px;font-size:11px;padding:10px 17px;line-height:1.2}
.news .head b{display:block;text-align:right;font-size:14px;font-weight:600}
.news .item{position:absolute;left:20px;width:170px;font-size:7.5px;line-height:1.45}
.news .item i{display:block;margin-bottom:4px;font-size:8px}
.news .item u{display:block;text-align:right;margin-top:5px;font-style:italic}
.footer{left:166px;top:1073px;width:761px;height:127px;border-top:3px solid var(--navy)}
.fcol{top:1088px;font-size:7.5px;line-height:15px;color:var(--ink)}
.fcol h4{font-size:13px;font-weight:600;color:var(--tan-dark);margin-bottom:4px;line-height:18px}
.fcol li{list-style:none}
.fcol li::before{content:"» ";color:var(--green)}
.flogo{left:750px;top:1118px;font-size:22px;font-weight:600;display:flex;gap:8px;align-items:center}
.flogo .dot{width:20px;height:20px;border-radius:50%;background:var(--gold)}
</style>
</head>
<body>
<div class="backdrop" role="img" aria-label="Photo of a school marching band on a baseball stadium field"></div>
<div class="page"></div>

<div class="abs logo"><span class="dot"></span>RIDGE HORN</div>
<div class="abs toplinks"><span>Wish List (0)</span><span>My Account</span><span>Shopping Cart</span><span>Checkout</span><span class="login">Login | Register</span></div>
<svg class="abs" style="left:850px;top:22px" width="26" height="24" viewBox="0 0 26 24"><path d="M1 4h4l3 12h13l3-9H7" fill="none" stroke="#777" stroke-width="2"/><circle cx="10" cy="20" r="2" fill="#777"/><circle cx="19" cy="20" r="2" fill="#777"/><circle cx="21" cy="5" r="5" fill="var(--gold)"/></svg>
<div class="abs currency">$ ⌄</div>
<div class="abs phone"><svg width="15" height="15" viewBox="0 0 16 16"><circle cx="8" cy="8" r="7" fill="none" stroke="#b0905a" stroke-width="1.5"/><path d="M8 4v4l3 2" stroke="#b0905a" stroke-width="1.5" fill="none"/></svg>555 210 4418</div>

<nav class="abs nav"><a style="width:79px">Home</a><a style="width:103px">About Us</a><a style="width:122px">Instruments</a><a style="width:100px">Buy /Sell</a><a style="border:0">Contact Us</a></nav>
<div class="abs search">Search<svg style="position:absolute;right:8px;top:4px" width="13" height="13" viewBox="0 0 13 13"><circle cx="5" cy="5" r="4" fill="none" stroke="#222" stroke-width="1.6"/><path d="M8 8l4 4" stroke="#222" stroke-width="1.8"/></svg></div>

<div class="abs slide" role="img" aria-label="Close-up of brass horns and a violin with bow"></div>
<div class="abs caption">Donec arcu dolor, sodales ut lobortis adipiscing, auctor id purus.</div>
<div class="abs arrowbtn" style="left:629px">‹</div>
<div class="abs arrowbtn" style="left:655px">›</div>

<div class="abs promo" style="top:152px;height:128px;background:var(--tan)">
  <div style="position:absolute;left:0;top:0;width:60px;height:46px;background:#fbfbfa"></div>
  <div class="head">Music Teachers<b>AVAILABLE</b></div>
  <div class="body">Nulla egestas mi non pulvinar sodales. Vesti bulum id luctus augue. Integer sem nisl, susc ipit sit amet cursus non, venenatis</div>
  <div class="go">➜</div>
</div>
<div class="abs promo" style="top:300px;height:127px;background:linear-gradient(180deg,#c9a33c,#dcb443)">
  <div style="position:absolute;left:0;top:0;width:60px;height:46px;background:#fbfbfa"></div>
  <div class="head">Music Products<b>HIGHLIGHTS</b></div>
  <div class="body">Nulla egestas mi non pulvinar sodales. Vesti bulum id luctus augue. Integer sem nisl, susc ipit sit amet cursus non, venenatis Praesent aliquet mauris ante.</div>
  <div class="go">➜</div>
</div>

<div class="abs barhead" style="left:182px;top:454px;width:203px;background:linear-gradient(180deg,#d6a93a,#c2922c)">CATEGORIES</div>
<div class="abs barhead" style="left:427px;top:454px;width:483px;background:var(--tan)">FEATURED PRODUCTS</div>

<ul class="abs cats">
  <li>Praesent eget purus eu</li><li>massa rutrum blandit. In viverra,</li><li>augue vitae facilisis hendrerit,</li><li>mauris sem suscipit nisi, et rutrum nibh</li><li>quam at felis. Mauris viverra at</li><li>mauris sed malesuada</li><li>Phasellus augue urna, tristique et</li><li>porta eget, rhoncus at diam Suspendisse</li><li>mollis enim nec lorem consectetu</li>
</ul>

<div class="abs card" style="left:429px;top:505px"><div class="img" role="img" aria-label="Alto saxophone"></div><div class="stars">★★★☆☆</div><h3>Alto Sax</h3><p>vitae adipiscing urna accumsan<br>vitae. Nunc varius nunc ut nisl</p><div class="price">$249.99</div><div class="cart">Add to Cart</div><div class="mini" style="left:88px">▁▃▅</div><div class="mini" style="left:110px">☆</div></div>
<div class="abs card" style="left:597px;top:505px"><div class="img" role="img" aria-label="Trombone"></div><div class="stars">★★★☆☆</div><h3>Trombone</h3><p>vitae adipiscing urna accumsan<br>vitae. Nunc varius nunc ut nisl</p><div class="price">$249.99</div><div class="cart">Add to Cart</div><div class="mini" style="left:88px">▁▃▅</div><div class="mini" style="left:110px">☆</div></div>
<div class="abs card" style="left:765px;top:505px"><div class="img" role="img" aria-label="Clarinet" style="background:radial-gradient(ellipse,#444,#f4f4f4 70%)"></div><div class="stars">★★★☆☆</div><h3>Clarinet</h3><p>vitae adipiscing urna accumsan<br>vitae. Nunc varius nunc ut nisl</p><div class="price">$249.99</div><div class="cart">Add to Cart</div><div class="mini" style="left:88px">▁▃▅</div><div class="mini" style="left:110px">☆</div></div>

<div class="abs card" style="left:429px;top:786px"><div class="img" role="img" aria-label="Baritone horn"></div><div class="stars">★★★☆☆</div><h3>Baritone</h3><p>vitae adipiscing urna accumsan<br>vitae. Nunc varius nunc ut nisl</p><div class="price">$249.99</div><div class="cart">Add to Cart</div><div class="mini" style="left:88px">▁▃▅</div><div class="mini" style="left:110px">☆</div></div>
<div class="abs card" style="left:597px;top:786px"><div class="img" role="img" aria-label="Trumpet"></div><div class="stars">★★★☆☆</div><h3>Trumpet</h3><p>vitae adipiscing urna accumsan<br>vitae. Nunc varius nunc ut nisl</p><div class="price">$249.99</div><div class="cart">Add to Cart</div><div class="mini" style="left:88px">▁▃▅</div><div class="mini" style="left:110px">☆</div></div>
<div class="abs card" style="left:765px;top:786px"><div class="img" role="img" aria-label="Tenor saxophone"></div><div class="stars">★★★☆☆</div><h3>Tenor Sax</h3><p>vitae adipiscing urna accumsan<br>vitae. Nunc varius nunc ut nisl</p><div class="price">$249.99</div><div class="cart">Add to Cart</div><div class="mini" style="left:88px">▁▃▅</div><div class="mini" style="left:110px">☆</div></div>

<div class="abs news">
  <div style="position:absolute;left:0;top:0;width:53px;height:42px;background:#fbfbfa;color:#111;font-size:30px;text-align:center;line-height:42px">♫</div>
  <div class="head">Music News &amp;<b>EVENTS</b></div>
  <div class="item" style="top:62px"><i>23-Jun-2014</i>Nulla egestas mi non pulvinar sodales. Vesti bulum id luctus augue. Integer sem nisl, susc ipit sit amet cursus non, venenatis<u>View detail »</u></div>
  <div class="item" style="top:141px"><i>23-Jun-2014</i>Nulla egestas mi non pulvinar sodales. Vesti bulum id luctus augue. Integer sem nisl, susc ipit sit amet cursus non, venenatis<u>View detail »</u></div>
  <div class="go" style="position:absolute;right:0;bottom:0;width:31px;height:19px;background:#fff;color:var(--red);font-size:12px;text-align:center;line-height:19px">➜</div>
</div>

<div class="abs footer"></div>
<div class="abs fcol" style="left:185px"><h4>Information</h4><ul><li>About</li><li>Delivery</li><li>Privacy Policy</li><li>Terms &amp; Conditions</li></ul></div>
<div class="abs fcol" style="left:322px"><h4>Customer Service</h4><ul><li>Contact Us</li><li>Returns</li><li>Site Map</li></ul></div>
<div class="abs fcol" style="left:492px"><h4>Extras</h4><ul><li>Brands</li><li>Gift Vouchers</li><li>Affiliates</li><li>Specials</li></ul></div>
<div class="abs fcol" style="left:615px"><h4>My Account</h4><ul><li>My Account</li><li>Order History</li><li>Wish List</li><li>Newsletter</li></ul></div>
<div class="abs flogo"><span class="dot"></span>RIDGE HORN</div>
</body>
</html>
```